Occasions chocolate packaging

We are looking for 7 packaging designs for bars of chocolate.

Each design needs to be different and we’re not looking for a consistent brand or branding message across the designs. Inspiration should come from gift/occasion cards. Fun, simple, bold, vibrant colours and eye catching, i.e. not vintage or just text.

The front of the packaging should have the main message on and is free of any branding. You don’t need to design the back, just simply allow the main background colour or design pattern to continue around.

These are the different designs we are after, I’ve added in some text for each to give you some guidance but feel free to play around with the message if it suits the design better.

1) Mum
‘The best mum’, ‘Best mum in the World’, ‘Number 1 Mum’

2) Dad
‘The Best Dad’, ‘Best Dad Ever’, ‘Number 1 Dad’, ‘You’re my hero Dad’

3) Husband
‘Best Husband in the World’, ‘Husband I Love You’, ‘Darling Husband’

4) Wife
‘Best Wife in the World’, ‘For my Wonderful Wife’, ‘My Beautiful Wife’

5) Congratulations
Simple one, just Congratulations

6) Thinking of you
Try and keep this neutral as it could be used for happy and sad situations.

7) Thank you
Keep this gender neutral.

Sides:
The sides need to have the following text:

FINE BELGIAN DARK CHOCOLATE
infused with Orange

Back:
The main colour of the front should continue all the way around, we will place a box with the contents and bar code on here ourselves so no need to do anything.

Dimensions:
Attached in the document, front of package is 85mm by 190mm.

The packaging is made from folded card, the first blank part is for gluing the back on to.

Reason: I'm extending the deadline as I've only received 1 design so far which has followed the brief. Although I do like it, I would like to see at least some competition...

```html
<!DOCTYPE html>
<html lang="en">
<head>
<meta charset="utf-8">
<title>Occasions chocolate packaging</title>
<link rel="stylesheet" href="https://fonts.googleapis.com/css2?family=Amatic+SC:wght@700&family=Dancing+Script:wght@500&family=Kaushan+Script&family=Montserrat:wght@400;900&family=Oswald:wght@300;400;500&family=Raleway:wght@500&display=swap">
<style>
:root{
  --mum-pink:#ff8385;
  --mum-soft:#ffc4c6;
  --mum-yellow:#fecb0a;
  --mum-teal:#2a8f8c;
  --thanks-yellow:#ebcb52;
  --thanks-teal:#0bb3bc;
  --thanks-mint:#9ed8d6;
  --thanks-cream:#f4e3a4;
  --thanks-gold:#f2b829;
  --congrats-purple:#862f96;
  --congrats-pink:#e8206e;
  --congrats-yellow:#f7c500;
  --congrats-teal:#19aab0;
  --congrats-sky:#7ec8ea;
  --white:#ffffff;
  --fold:rgba(255,255,255,.35);
}
*{margin:0;padding:0;box-sizing:border-box}
html,body{width:1200px;height:1000px;overflow:hidden;background:#fff}
.canvas{position:relative;width:1200px;height:1000px}
.dieline{position:absolute;width:486px;height:451px;overflow:hidden;color:var(--white)}
.dieline--mum{left:96px;top:37px;background:var(--mum-pink)}
.dieline--thanks{left:618px;top:38px;background:var(--thanks-yellow)}
.dieline--congrats{left:362px;top:512px;background:var(--congrats-purple)}
.fold{position:absolute;top:0;bottom:0;width:1px;background:var(--fold)}
.side-copy{position:absolute;bottom:128px;writing-mode:vertical-rl;transform:rotate(180deg);white-space:nowrap;font-size:10px;line-height:1}
.side-copy .caps{font-size:11px}
.side-copy .brush{font-size:11px}
.front{position:absolute;top:0;bottom:0;width:225px}
.caps{font-family:"Amatic SC",sans-serif;font-weight:700}
.script{font-family:"Dancing Script",cursive;font-weight:500}
.brush{font-family:"Kaushan Script",cursive}
.bold-script{font-family:"Kaushan Script",cursive;font-size:11px}

/* mum */
.mum-floral{position:absolute;left:0;top:12px;width:225px;height:300px}
.mum-badge{position:absolute;left:27px;top:88px;width:148px;height:148px;border-radius:50%;background:var(--mum-yellow);border:3px solid var(--white);text-align:center}
.mum-badge .no{display:block;margin-top:18px;font-family:"Oswald",sans-serif;font-weight:300;font-size:44px;line-height:1;color:var(--mum-teal);letter-spacing:-2px}
.mum-badge .no b{font-weight:500;color:var(--mum-pink);font-size:52px}
.mum-badge .word{display:block;font-family:"Kaushan Script",cursive;font-size:44px;line-height:.9;color:var(--white)}
.mum-words{position:absolute;left:0;top:308px;width:225px;text-align:center;font-size:13px;line-height:14.5px;white-space:nowrap}
.mum-words .caps{font-size:13px}

/* thanks */
.ribbon{position:absolute;left:25px;top:0}
.thanks-stack{position:absolute;left:15px;top:10px;width:176px;text-align:center;font-family:"Kaushan Script",cursive;font-size:37px;line-height:55px;letter-spacing:-1px;white-space:nowrap}
.thanks-stack .t1{color:var(--thanks-mint)}
.thanks-stack .t2{color:var(--thanks-cream)}
.thanks-stack .t3{color:var(--thanks-gold)}
.thanks-stack .t4{color:var(--white);font-size:40px}
.thanks-words{position:absolute;left:0;top:302px;width:203px;text-align:center;font-size:13px;line-height:16px;white-space:nowrap}
.thanks-words .caps{font-size:14px}

/* congrats */
.congrats-type{position:absolute;left:0;top:0;width:203px}
.c-con{position:absolute;left:20px;top:12px;font-family:"Montserrat",sans-serif;font-weight:900;font-size:68px;letter-spacing:-3px;color:var(--congrats-pink);line-height:1}
.c-gra{position:absolute;left:22px;top:50px;font-family:"Kaushan Script",cursive;font-size:86px;color:var(--congrats-yellow);line-height:1}
.c-tul{position:absolute;left:48px;top:122px;font-family:"Oswald",sans-serif;font-weight:400;font-size:88px;line-height:1;letter-spacing:-1px}
.c-ati{position:absolute;left:20px;top:220px;font-family:"Montserrat",sans-serif;font-weight:900;font-size:82px;line-height:1;letter-spacing:-4px;color:var(--congrats-teal)}
.c-ons{position:absolute;left:24px;top:282px;font-family:"Oswald",sans-serif;font-weight:500;font-size:104px;line-height:1;color:transparent;-webkit-text-stroke:3px var(--congrats-sky)}
.balloon{position:absolute}
.c-wave{position:absolute;left:0;top:368px}
.c-caption{position:absolute;left:0;top:418px;width:203px;text-align:center;font-family:"Raleway",sans-serif;font-weight:500;font-size:14px}
</style>
</head>
<body>
<div class="canvas">

  <section class="dieline dieline--mum">
    <span class="fold" style="left:36px"></span>
    <span class="fold" style="left:59px"></span>
    <span class="fold" style="left:284px"></span>
    <p class="side-copy" style="left:40px"><span class="caps">FINE BELGIAN DARK CHOCOLATE</span> · <span class="brush">infused with Orange</span></p>
    <p class="side-copy" style="left:268px"><span class="caps">FINE BELGIAN DARK CHOCOLATE</span> · <span class="brush">infused with Orange</span></p>
    <div class="front" style="left:59px">
      <svg class="mum-floral" viewBox="0 0 225 300" role="img" aria-label="Wreath of leaves, flowers and swirls around the badge">
        <ellipse cx="112" cy="150" rx="108" ry="145" fill="var(--mum-soft)" opacity=".6"/>
      </svg>
      <div class="mum-badge"><span class="no">No.<b>1</b></span><span class="word">mum</span></div>
      <div class="mum-words">
        <span class="script">you're the best mum</span> &nbsp; <span class="caps">I LOVE YOU MUM</span><br>
        <span class="bold-script">the best mum</span> <span class="caps">THE GREATEST MUM IN THE WORLD</span><br>
        <span class="script">you're amazing mum</span><br>
        <span class="caps">WHEN I GROW UP, I WANT TO BE JUST LIKE YOU MUM</span><br>
        <span class="script">Number One Mum</span> <span class="bold-script">the best mum</span><br>
        <span class="bold-script">the best mum</span> <span class="caps">THE GREATEST MUM IN THE WORLD</span><br>
        <span class="script">you're amazing mum</span><br>
        <span class="caps">WHEN I GROW UP, I WANT TO BE JUST LIKE YOU MUM</span><br>
        <span class="bold-script">the best mum</span> <span class="script">Number One Mum</span>
      </div>
    </div>
  </section>

  <section class="dieline dieline--thanks">
    <span class="fold" style="left:35px"></span>
    <span class="fold" style="left:59px"></span>
    <span class="fold" style="left:262px"></span>
    <span class="fold" style="left:285px"></span>
    <p class="side-copy" style="left:38px"><span class="caps">FINE BELGIAN DARK CHOCOLATE</span> · <span class="brush">infused with Orange</span></p>
    <p class="side-copy" style="left:266px"><span class="caps">FINE BELGIAN DARK CHOCOLATE</span> · <span class="brush">infused with Orange</span></p>
    <div class="front" style="left:59px;width:203px">
      <svg class="ribbon" width="156" height="296" viewBox="0 0 156 296">
        <path d="M0 0H156V294L78 244L0 294Z" fill="var(--thanks-teal)"/>
        <path d="M6 0V282L78 236L150 282V0" fill="none" stroke="var(--white)" stroke-width="1" stroke-dasharray="4 3"/>
      </svg>
      <div class="thanks-stack">
        <div class="t1">Thankyou</div><div class="t2">Thankyou</div><div class="t3">Thankyou</div><div class="t4">Thankyou</div>
      </div>
      <div class="thanks-words">
        <span class="script">Danke</span> <span class="caps">DANKIE GRATIAS</span> <span class="bold-script">Merci</span> <span class="script">Haala</span><br>
        <span class="caps">CHOKRAN</span> <span class="script">Dank u</span> <span class="caps">VINAKA</span> <span class="bold-script">Grazias</span><br>
        <span class="bold-script">Grazie</span> <span class="caps">CHEERS</span> <span class="script">thanks</span> <span class="caps">CHOKRAN</span><br>
        <span class="script">Danke</span> <span class="caps">DANKIE GRATIAS</span> <span class="bold-script">Merci</span> <span class="script">Haala</span><br>
        <span class="caps">CHOKRAN</span> <span class="script">Dank u</span> <span class="caps">VINAKA</span> <span class="bold-script">Grazias</span><br>
        <span class="bold-script">Grazie</span> <span class="caps">CHEERS</span> <span class="script">thanks</span> <span class="caps">CHEERS</span><br>
        <span class="script">Danke</span> <span class="caps">DANKIE GRATIAS</span> <span class="bold-script">Merci</span> <span class="script">Haala</span><br>
        <span class="caps">CHOKRAN</span> <span class="script">Dank u</span> <span class="caps">VINAKA</span> <span class="bold-script">Grazias</span>
      </div>
    </div>
  </section>

  <section class="dieline dieline--congrats">
    <span class="fold" style="left:36px"></span>
    <span class="fold" style="left:59px"></span>
    <span class="fold" style="left:262px"></span>
    <span class="fold" style="left:285px"></span>
    <p class="side-copy" style="left:40px"><span class="caps">FINE BELGIAN DARK CHOCOLATE</span> · <span class="brush">infused with Orange</span></p>
    <p class="side-copy" style="left:266px"><span class="caps">FINE BELGIAN DARK CHOCOLATE</span> · <span class="brush">infused with Orange</span></p>
    <div class="front" style="left:59px;width:203px">
      <div class="congrats-type" aria-label="Congratulations">
        <span class="c-con">CON</span>
        <span class="c-gra">gra</span>
        <span class="c-tul">TUL</span>
        <span class="c-ati">ATI</span>
        <span class="c-ons">ONS</span>
      </div>
      <svg class="balloon" style="left:20px;top:156px" width="32" height="56" role="img" aria-label="Balloon with confetti"><rect width="32" height="56" fill="var(--congrats-pink)" opacity=".35"/></svg>
      <svg class="balloon" style="left:160px;top:104px" width="32" height="56" role="img" aria-label="Balloon with confetti"><rect width="32" height="56" fill="var(--congrats-pink)" opacity=".35"/></svg>
      <svg class="c-wave" width="203" height="44" viewBox="0 0 203 44">
        <path d="M0 28C25 8 50 8 75 24S125 40 150 22S190 6 203 12V22C190 16 172 18 150 32S100 50 75 34S25 18 0 38Z" fill="var(--white)"/>
      </svg>
      <p class="c-caption">CONGRATULATIONS</p>
    </div>
  </section>

</div>
</body>
</html>
```